Billboard

we want our Hop & Skip logo really big, we need this to stand out

Use a really bold font for the wording as it's on a billboard on the highway

Hop & Skip Logo
perhaps on left hand side really large then have a slanting line and a different colour background for the other side.

Wording BELOW-bold

TOUR NOW

hopandskip.edu.au

Use one image,
I have attached other designs we have been using for our campaign so a similar look would be great.
specs- 1224 W × 324 H px JPEG

Target Market(s)
families

Industry/Entity Type
childcare

Target Market(s)

families

Industry/Entity Type

childcare

Requirements
Must have
• bold font and big logo

```html
<!DOCTYPE html>
<html lang="en">
<head>
<meta charset="utf-8">
<title>Hop &amp; Skip – Tour Now Billboard</title>
<link rel="stylesheet" href="https://fonts.googleapis.com/css2?family=Montserrat:wght@600;800;900&display=swap">
<style>
  :root {
    --sky-blue: #00b6f0;
    --sun-yellow: #fdca3b;
    --tomato-red: #f4432f;
    --white: #ffffff;
    --stage: #e9ecef;
    --photo-warm: #d9a06a;
    --photo-green: #7c8a3c;
    --photo-teal: #2aa7c2;
  }
  html, body {
    margin: 0;
    padding: 0;
    width: 1200px;
    height: 1142px;
    overflow: hidden;
    background: var(--stage);
  }
  .billboard {
    position: absolute;
    left: 30px;
    top: 420px;
    width: 1140px;
    height: 302px;
    box-shadow: 0 10px 24px rgba(0,0,0,0.25);
  }
  .billboard svg {
    display: block;
    width: 100%;
    height: 100%;
  }
  .brand-name {
    font-family: "Montserrat", sans-serif;
    font-weight: 900;
    fill: var(--white);
  }
  .headline {
    font-family: "Montserrat", sans-serif;
    font-weight: 800;
  }
  .headline-tour { fill: var(--sky-blue); }
  .headline-now { fill: var(--tomato-red); }
  .web-address {
    font-family: "Montserrat", sans-serif;
    font-weight: 600;
    fill: var(--white);
  }
</style>
</head>
<body>
  <div class="billboard">
    <svg viewBox="0 0 1746 463" xmlns="http://www.w3.org/2000/svg">
      <defs>
        <linearGradient id="photoTones" x1="0" y1="0" x2="1" y2="1">
          <stop offset="0" stop-color="var(--photo-green)"/>
          <stop offset="0.45" stop-color="var(--photo-teal)"/>
          <stop offset="1" stop-color="var(--photo-warm)"/>
        </linearGradient>
      </defs>

      <!-- brand panel -->
      <rect class="brand-panel" x="0" y="0" width="1746" height="463" fill="var(--sky-blue)"/>

      <!-- photo area -->
      <g role="img" aria-label="Photo of toddlers in sun hats playing in a sandpit with a bucket">
        <polygon points="1123,0 1746,0 1746,463 1233,463 1328,287" fill="url(#photoTones)"/>
      </g>

      <!-- message chevron -->
      <polygon class="message-panel" points="545,0 1123,0 1328,287 1233,463 660,463 447,172"
               fill="var(--sun-yellow)" stroke="var(--white)" stroke-width="9" stroke-linejoin="round"/>

      <!-- web address band -->
      <polygon class="address-band" points="597,368 1285,368 1233,463 660,463" fill="var(--tomato-red)"/>
      <polyline points="597,368 660,463" fill="none" stroke="var(--white)" stroke-width="9"/>
      <polyline points="1285,368 1233,463" fill="none" stroke="var(--white)" stroke-width="9"/>

      <!-- brand name -->
      <text class="brand-name" x="225" y="200" font-size="100" text-anchor="middle">Hop &amp;</text>
      <text class="brand-name" x="225" y="318" font-size="100" text-anchor="middle">Skip</text>

      <!-- headline -->
      <text class="headline headline-tour" x="840" y="182" font-size="160" text-anchor="middle">TOUR</text>
      <rect class="highlight" x="655" y="218" width="495" height="122" fill="var(--white)"/>
      <text class="headline headline-now" x="905" y="318" font-size="130" text-anchor="middle">NOW</text>

      <!-- web address -->
      <text class="web-address" x="948" y="432" font-size="42" text-anchor="middle">www.hopandskip.edu.au</text>
    </svg>
  </div>
</body>
</html>
```